Business Card Design for company

We want new business cards. We'd like something different-- yet still highly professional. Our tagline is Providing leadership, delivering success. Stock photos are ok, as long as they are relevant and look upscale.

Target Market(s)

Architecture/Business Management Consulting/Engineering Consulting

Contact Information for Business Card

dark gray background with pops of blue might be good, but you tell me. You're the designers. Rounded corners might be nice, but again, you tell me.

Font styles to use
Serif
Sans Serif

Colors
3276b5
5c5c5c
9d9d9d
fbfbfb

Requirements
Nice to have
• Something different, but still very professional.

```html
<!DOCTYPE html>
<html lang="en">
<head>
<meta charset="utf-8">
<title>Altonridge Group – Business Card</title>
<link rel="stylesheet" href="https://fonts.googleapis.com/css2?family=Open+Sans:wght@400;600;700&display=swap">
<style>
  :root {
    --blue: #3276b5;
    --blue-deep: #2a64a0;
    --ink: #4a4d52;
    --gray: #5c5c5c;
    --gray-light: #9d9d9d;
    --paper: #fbfbfb;
    --stage: #3a3b3d;
  }
  * { box-sizing: border-box; margin: 0; padding: 0; }
  html, body {
    width: 1200px; height: 895px; overflow: hidden;
    background: var(--stage);
    font-family: "Open Sans", Arial, sans-serif;
  }
  .sheet {
    position: relative; width: 1200px; height: 895px;
    display: flex; align-items: center; justify-content: center; gap: 40px;
  }
  .card {
    position: relative; width: 540px; height: 309px;
    background: var(--paper); border-radius: 20px; overflow: hidden;
    box-shadow: 0 10px 28px rgba(0,0,0,.45);
  }

  /* Brand name block */
  .brand { color: var(--ink); font-weight: 600; line-height: 1; text-transform: uppercase; white-space: nowrap; }
  .brand-name { display: block; letter-spacing: .04em; }
  .brand-sub { display: block; letter-spacing: .18em; }

  /* Front */
  .card-front .brand { position: absolute; left: 0; right: 0; top: 92px; text-align: center; }
  .card-front .brand-name { font-size: 52px; }
  .card-front .brand-sub { font-size: 22px; margin-top: 12px; }
  .web-rule {
    position: absolute; left: 0; right: 0; bottom: 46px;
    display: flex; align-items: center; gap: 12px;
  }
  .web-rule::before, .web-rule::after {
    content: ""; flex: 1; height: 1.5px; background: var(--blue);
  }
  .web-rule span { font-size: 13px; letter-spacing: .12em; color: var(--ink); }
  .web-rule em { font-style: normal; color: var(--blue); }

  /* Back */
  .details {
    position: absolute; left: 36px; top: 48px; width: 250px;
    text-align: right; color: #2f3134;
  }
  .group { position: relative; padding-right: 18px; margin-bottom: 14px; }
  .group::after {
    content: ""; position: absolute; right: 0; top: 2px; bottom: 2px;
    width: 1.5px; background: var(--gray);
  }
  .group.accent::after { background: var(--blue); }
  .person-name { font-size: 21px; font-weight: 700; color: var(--blue); letter-spacing: .04em; }
  .person-role { font-size: 13px; }
  .address p, .contact li { font-size: 13px; line-height: 1.45; }
  .contact { list-style: none; }
  .contact li { display: flex; justify-content: flex-end; align-items: center; gap: 7px; }
  .contact svg { width: 11px; height: 11px; fill: var(--blue); flex: none; }

  .card-back .brand { position: absolute; left: 306px; right: 22px; top: 66px; }
  .card-back .brand-name { font-size: 28px; letter-spacing: .02em; }
  .card-back .brand-sub { font-size: 14px; margin-top: 8px; letter-spacing: .22em; }

  .swoosh { position: absolute; left: 0; bottom: 0; width: 540px; height: 140px; }
</style>
</head>
<body>
<main class="sheet">

  <section class="card card-front" aria-label="Card front">
    <div class="brand">
      <span class="brand-name">Altonridge</span>
      <span class="brand-sub">Group</span>
    </div>
    <div class="web-rule"><span>www.<em>altonridgegroup</em>.com</span></div>
  </section>

  <section class="card card-back" aria-label="Card back">
    <div class="details">
      <div class="group">
        <p class="person-name">DANIEL REYES</p>
        <p class="person-role">Director</p>
      </div>
      <div class="group accent address">
        <p>48 Harbor Lane</p>
        <p>Cedar Falls, OR 97310</p>
      </div>
      <ul class="group contact">
        <li>(014) 552-0187
          <svg viewBox="0 0 24 24" aria-hidden="true"><path d="M6.6 10.8a15 15 0 0 0 6.6 6.6l2.2-2.2c.3-.3.7-.4 1-.2 1.1.4 2.3.6 3.6.6.6 0 1 .4 1 1V20c0 .6-.4 1-1 1A17 17 0 0 1 3 4c0-.6.4-1 1-1h3.5c.6 0 1 .4 1 1 0 1.3.2 2.5.6 3.6.1.3 0 .7-.2 1z"/></svg></li>
        <li>info@altonridgegroup.com
          <svg viewBox="0 0 24 24" aria-hidden="true"><path d="M2 5h20v14H2zm2 2v.5l8 5 8-5V7z"/></svg></li>
        <li>www.altonridgegroup.com
          <svg viewBox="0 0 24 24" aria-hidden="true"><circle cx="12" cy="12" r="10"/></svg></li>
      </ul>
    </div>

    <div class="brand">
      <span class="brand-name">Altonridge</span>
      <span class="brand-sub">Group</span>
    </div>

    <svg class="swoosh" viewBox="0 0 540 140" preserveAspectRatio="none" aria-hidden="true">
      <path d="M0 140 L0 96 C120 70 300 60 540 0 L540 140 Z" fill="var(--gray)"/>
      <path d="M0 140 L0 108 C130 80 310 70 540 16 L540 140 Z" fill="var(--paper)"/>
      <path d="M0 140 L0 114 C140 88 320 78 540 24 L540 140 Z" fill="var(--blue)"/>
    </svg>
  </section>

</main>
</body>
</html>
```